Near future techno-thriller needs a mind blowing book cover design!

The Hollow Tonic is the first in a trilogy of techno thrillers set in a very recognisable near future.

The world is changing. A mass market drug promised to boost intelligence. The world embraced it and soon everyone was a genius, but only for a while. The long term effects crippled the world societies. A select few experience much greater changes, becoming something more than human.

The book paints a Rustcanyon like future, a society on the verge of collapse. The only two known posthumans are fighting an incomprehensible war against each other. Carl Brisket, an old fashioned private investigator who is slowly losing his mental faculties as a result of the Drug, is tasked with capturing one of them.

This is a book that ask the question what we might become in the future, if our intellects expanded to the point where the boundaries of intellect no longer apply.

The winning designer will also be used for the second and third book in the series.

Author's name is "Henrik Ålmgård"

MAIN CHARACTERS
Beyond the meta humans, there are two other main characters. This is the description from the book:

Carl Brisket
Carl Brisket is a private investigator in a world where they are no longer needed.

"FenLo studied the man next to him. Carl was asleep or at least it looked that way – his face always seemed set in a frown. Now that he was relaxed, half lying down in the car seat, he looked so old. FenLo knew he was thirty-six, but looked closer to fifty. His dark hair was turning grey. FenLo had seen photos of Carl in his mid-twenties. He had been quite handsome, making it hard to imagine what could have happened. Now he looked like an ageing movie star that had let himself go."

FenLo
FenLo is an operative for a posthuman interest group. He is an expert hacker and also a skilled stick fighter.

"A single streetlight created a cone of light in the centre of the playground, with everything else dimming into darkness. A young man was sitting on one of the swings, dangling his legs back and forth motionless. Like most people under 25, he had a completely integrated uPalo, and it was obvious he was doing something with it. From the occasional twitches in his fingers, Carl guessed he was playing a game. Carl approached him slowly, wondering if he’d come to the right place. As he got closer, he no longer had any doubts. The boy was of Asian descent and the spitting image of his father. He wore baggy pants and a black hoodie with a swirling pattern emanating from the chest. Expensive clothes designed to imitate what actual street kids wore. Carl hated the pretence.
As the more integrated systems almost completely disconnected you from what was going on around you, the uPalo allowed greetings that interrupted the current activity. Carl never had much time for such niceties. He walked up to the pretend gangster and tapped him on the forehead. The young man jolted backwards, tangled up in the swing and fell in a heap."

PROBABILITY MATRIX
One of the core concepts in the book is the idea of a probability matrix available to the posthumans. A mind map of decisions and probabilities. This concept would be interesting to see as the basis for the cover, or maybe the background, with a figure (either a posthuman or the private investigator) in the foreground. Here is a description from the book:

“Is this death?” Carl thought, his mind suspended in darkness.
A single light far away caught his attention. Was this the tunnel of light so common in near-death experiences? He focused on the light and willed himself to move towards it.
Nothing happened. He remained where he was as another light and then another appeared. At first they seemed random, but as they multiplied, thin strands of light connected them until what looked like a major city seen from above at night spread out below him.
It reminded him of the mind maps he could see when he was on the Drug, except much more complex. He no longer tried to move. He knew he was the centre of this space - everything else would move. He willed the map to take him to the beginning, that solitary spot he had first seen.
The dot represented his birth. All light surrounding him represented actions or decisions affecting him. Lines of varying colours and intensity led from this single dot to others, representing the probability.
He wanted to remain here to explore, but a distant pulsating light drew his attention. He travelled forward to now and studied the end of his life. To his surprise it didn’t end. From the current time there was a decision point with only a ten percent likelihood of death. The outgoing lines suggested many options. One in particular interested him as it had a high probability and included a line that seemed to depart from the matrix altogether. He followed it and a new matrix opened. This time the nodes were no longer decision points in his life. They were codes that translated to locations, people and devices as he studied them. It was a network diagram based on what he could access….

POSTHUMANS
Another core concept is the postHumans. They are people who has had their minds enhanced by the drug, but this is just the starting point. In the book one of the postHumans become a distributed mind, across multiple bodies. Another starts reconfiguring their body. Below are two sections from the book detailing this:

"Marva had made a remarkable recovery. Her skin had regenerated, shedding the old burnt one like sunburnt skin. The new skin was harder, more akin to a reptile’s, which made even taking blood samples difficult. Not that he knew what to do with them any longer, anyway. Most of her bodily processes had changed. She was still human, but only in the same sense that a Velocar Prime car was a car. He suspected this was not a direct result of CereVox, but only a follow-on effect. The Drug had opened the door, but Marva was the architect behind the modifications, whether consciously or unconsciously. She had been killed, but managed to keep her body in a suspended state until the base functions could repair themselves and harden her body for any future attacks."

"My subconscious had begun a reconfiguration of what I was – a body to match the intellect it housed. It hadn’t even occurred to me until now that I could examine my body and its automatic processes in much the same as I could examine anything else.
What a marvelous machine it is, and yet so flawed.
It took only a cursory examination to question the possible involvement of a creator in its design. The mystery – if there was one – was how we had progressed this far at all. The spine was a prime example. It was an amazing construction for movement, but was obviously not for walking upright. Mine was reinforced, limiting movement somewhat. This was an understandable trade-off. Most of my physical enhancements, I discovered, were to better protect the brain and basic movement whilst limiting agility somewhat.
As I studied the different layers of the body, I found adjustments everywhere.
My metabolism had changed. I was now a hybrid with an organ specifically designed to store energy to feed my ever-increasing mind. Instead of allowing high-energy food such as sugars to flood my system, it stored them like a battery and released them as needed.
I had already seen the difference in analytics and critical thinking. The brain is an amazing organ, but to deal with the constant barrage of data and make sense of it, it filters, fills in the blanks and makes assumptions. My brain no longer did this. Instead it processed all information, made all the necessary connections and fed the result into the probability matrix.
The most surprising changes I found were in the building blocks of who I was. A completely new process was reprogramming my genome using designed viruses as the tool. A new organ created viruses and released them into the body. It changed the cell by infecting it, reprogramming all the cells in my body continuously. It was correcting deficiencies in my DNA."

Target Market(s)

From a cover perspective the book needs to capture readers who like near future sci-fi and techno thrillers. Here are some examples that have the right idea, but maybe slightly cheap looking approach:

http://www.pelmarobooks.com.au/The-Ember-Mind-Vantage-Series-ebook/dp/K47QX2MZRT/ref=pd_sim_351_2?ie=UTF8&refRID=5H2KP8LMQ3RTZWX4NB7C

http://www.pelmarobooks.com.au/drift-Tallow-Meridian-Book-ebook/dp/K39VW8RTYP/ref=pd_sim_351_2?ie=UTF8&refRID=6Q8DZ3HJT5MXCL2PVA09

Here is another that has similar themes:

http://www.pelmarobooks.com.au/Quorra-The-Trilogy-Book-ebook/dp/K52LHX4NWQ/ref=pd_sim_351_2?ie=UTF8&refRID=2D7FK9MBRS4JTUE6YHAL

Industry/Entity Type

Drug

Requirements
Must have
• This is an eBook cover for a kindle. I also need a standard sized cover with spine and back cover. The back cover blurb:
• “You may wonder why I tell you this, but bear with me. I didn’t realize it then, but I had stumbled on something of enormous importance. Something that will redefine mankind. Something that could redefine you.”
• Lucian – postHuman
• The world is changing. A mass market drug promised to boost intelligence. The world embraced it and soon everyone was a genius, but only for a while. The long term effects crippled the world societies. A select few experience much greater changes, becoming something more than human.
• Carl Brisket is hired by the very medical company that introduced the drug in the first place, to capture one of the posthumans. He finds himself part of a new world rising from the ashes of the old.
• The Hollow Tonic is a scif-fi thriller set in a very recognisable near future.

```html
<!DOCTYPE html>
<html lang="en">
<head>
<meta charset="utf-8">
<title>The Hollow Tonic — Henrik Ålmgård</title>
<link rel="stylesheet" href="https://fonts.googleapis.com/css2?family=Share+Tech+Mono&display=swap">
<style>
  :root {
    --paper: #ffffff;
    --stage: #ffffff;
    --ink: #111111;
    --line-grey: #9c9c9c;
    --pattern-light: #c9c9c9;
    --pattern-dark: #8f8f8f;
  }
  * { margin: 0; padding: 0; box-sizing: border-box; }
  html, body {
    width: 1200px;
    height: 900px;
    overflow: hidden;
    background: var(--stage);
  }
  .stage {
    position: relative;
    width: 1200px;
    height: 900px;
  }
  .front-cover {
    position: absolute;
    left: 320px;
    top: 20px;
    width: 560px;
    height: 860px;
    background: var(--paper);
    box-shadow: 0 0 0 1px #e4e4e4;
    overflow: hidden;
  }
  .cover-graphics {
    position: absolute;
    inset: 0;
    width: 100%;
    height: 100%;
  }
  .guide-line {
    stroke: var(--line-grey);
    stroke-width: 2;
    fill: none;
  }
  .title-block {
    position: absolute;
    right: 24px;
    top: 250px;
    text-align: right;
    font-family: "Share Tech Mono", monospace;
    font-weight: 400;
    color: var(--ink);
  }
  .book-title {
    font-weight: 400;
    font-size: 86px;
    line-height: 94px;
    letter-spacing: 2px;
    text-transform: uppercase;
  }
  .book-title .line { display: block; }
  .author-name {
    margin-top: 10px;
    font-size: 32px;
    line-height: 40px;
    letter-spacing: 1px;
    text-transform: uppercase;
  }
</style>
</head>
<body>
<main class="stage">
  <section class="front-cover">
    <svg class="cover-graphics" viewBox="0 0 560 860" xmlns="http://www.w3.org/2000/svg">
      <defs>
        <linearGradient id="circuit-tone" x1="0" y1="0" x2="1" y2="0">
          <stop offset="0" stop-color="#c9c9c9"/>
          <stop offset="1" stop-color="#8f8f8f"/>
        </linearGradient>
      </defs>

      <g class="probability-lines">
        <line class="guide-line" x1="175" y1="150" x2="440" y2="0"/>
        <line class="guide-line" x1="185" y1="70" x2="185" y2="0"/>
        <line class="guide-line" x1="175" y1="180" x2="560" y2="170"/>
        <line class="guide-line" x1="150" y1="690" x2="560" y2="680"/>
        <line class="guide-line" x1="320" y1="740" x2="320" y2="860"/>
        <line class="guide-line" x1="320" y1="760" x2="560" y2="750"/>
      </g>

      <path role="img" aria-label="Vertical band of grey circuit-board pattern breaking apart along its right edge"
        fill="url(#circuit-tone)"
        d="M0 0 H95 V40 H130 V70 H110 V110 H150 V150 H120 V190 H165 V235 H140 V275 H175 V300 H150 V345 H120 V380 H160 V420 H130 V460 H155 V500 H115 V540 H140 V585 H110 V625 H150 V665 H120 V705 H100 V745 H130 V790 H95 V830 H115 V860 H0 Z"/>
    </svg>

    <div class="title-block">
      <h1 class="book-title">
        <span class="line">The</span>
        <span class="line">Hollow</span>
        <span class="line">Tonic</span>
      </h1>
      <p class="author-name">Henrik Ålmgård</p>
    </div>
  </section>
</main>
</body>
</html>
```